Marbleton Health group for a medical office

We need a website created that for our new medical office that will support online booking for appointments. You designed the logo already.

```html
<!DOCTYPE html>
<html lang="en">
<head>
<meta charset="utf-8">
<title>Marbleton Health Group – Website</title>
<link href="https://fonts.googleapis.com/css2?family=Plus+Jakarta+Sans:wght@400;500;600;700&display=swap" rel="stylesheet">
<style>
:root{
  --board:#4a4a4a;
  --page:#f5f7f8;
  --surface:#ffffff;
  --line:#e4e9ec;
  --teal:#2c5f62;
  --teal-deep:#234f52;
  --ink:#16202a;
  --ink-soft:#3f6f80;
  --muted:#8a9aa3;
  --tint:#eef2f5;
  --track:#e6ecef;
  --star:#f2b72c;
}
*{box-sizing:border-box;margin:0;padding:0}
html,body{width:1200px;height:960px;overflow:hidden}
body{background:var(--board);font-family:"Plus Jakarta Sans",Arial,sans-serif;color:var(--ink);position:relative}
.panel{position:absolute;background:var(--page);overflow:hidden}
.panel *{position:absolute}
.panel .flow,.panel .flow *{position:static}
.home{left:24px;top:29px;width:564px;height:902px}
.book-one{left:612px;top:29px;width:564px;height:375px}
.book-two{left:612px;top:437px;width:564px;height:363px}

/* header */
.site-header{left:0;top:0;width:100%;height:29px;border-bottom:1px solid var(--line);background:var(--page)}
.brand{left:76px;top:7px;height:16px;display:flex;align-items:center;gap:4px}
.brand,.brand *{position:static}
.brand-mark{width:11px;height:11px;background:var(--teal);border-radius:2px}
.brand-name{font-size:9px;font-weight:700;color:var(--teal);letter-spacing:.2px;white-space:nowrap}
.nav{display:flex;gap:13px;font-size:5px;font-weight:500;color:var(--ink);top:12px}
.nav *{position:static}
.home .nav{left:316px}
.btn-nav{left:441px;top:8px;width:50px;height:14px;border-radius:2px;background:var(--teal);color:#fff;font-size:5px;font-weight:600;display:flex;align-items:center;justify-content:center}
.book-one .nav,.book-two .nav{left:349px}
.nav .active{color:var(--teal);font-weight:600;border-bottom:1px solid var(--teal);padding-bottom:2px}
.avatar-btn{left:469px;top:7px;width:14px;height:14px;border-radius:50%;background:#e8edf0;display:flex;align-items:center;justify-content:center}
.avatar-btn svg{position:static}

/* hero */
.badge{left:76px;top:58px;height:9px;padding:0 4px;border-radius:5px;background:#e3eae9;color:var(--teal);font-size:4.2px;font-weight:700;letter-spacing:.3px;line-height:9px}
.hero-title{left:76px;top:75px;width:200px;font-size:23px;line-height:27px;font-weight:700;letter-spacing:-.5px;color:var(--ink)}
.hero-text{left:76px;top:158px;width:175px;font-size:6.4px;line-height:10.5px;color:var(--ink-soft)}
.btn-primary{left:76px;top:199px;width:75px;height:20px;border-radius:3px;background:var(--teal);color:#fff;font-size:5.8px;font-weight:600;display:flex;align-items:center;justify-content:center}
.btn-ghost{left:156px;top:199px;width:61px;height:20px;border-radius:3px;background:#fff;border:1px solid var(--line);font-size:5.8px;font-weight:600;display:flex;align-items:center;justify-content:center}
.hero-rule{left:76px;top:227px;width:186px;height:1px;background:var(--line)}
.patients{left:76px;top:231px;display:flex;align-items:center}
.patients *{position:static}
.dot-face{width:13px;height:13px;border-radius:50%;border:1px solid #fff;margin-right:-3px}
.patients p{margin-left:9px;font-size:4.6px;color:var(--ink-soft)}
.patients b{color:var(--ink);font-weight:600}
.hero-photo{left:288px;top:96px;width:200px;height:113px;border-radius:4px;background:linear-gradient(100deg,#dfe3dd 0%,#f4f4f2 45%,#ececea 100%);box-shadow:0 6px 14px rgba(20,40,40,.18)}

/* services */
.section-title{left:76px;top:285px;font-size:12px;font-weight:700;color:var(--ink)}
.section-bar{left:76px;top:302px;width:28px;height:2px;border-radius:1px;background:var(--teal)}
.svc{top:317px;width:96px;height:75px;background:#fff;border:1px solid var(--line);border-radius:3px}
.svc .ico{left:8px;top:8px;width:17px;height:17px;border-radius:3px;background:#e8efef;display:flex;align-items:center;justify-content:center}
.svc .ico svg{position:static}
.svc h3{left:8px;top:33px;font-size:6.4px;font-weight:600;color:var(--ink)}
.svc p{left:8px;top:45px;width:80px;font-size:4.7px;line-height:7.6px;color:var(--ink-soft)}

/* why */
.why-band{left:76px;top:438px;width:413px;height:90px;background:var(--tint)}
.why-title{left:76px;top:445px;width:413px;text-align:center;font-size:12.5px;line-height:16.5px;font-weight:700;letter-spacing:-.2px}
.why-text{left:76px;top:505px;width:413px;text-align:center;font-size:6.2px;line-height:10px;color:var(--ink-soft)}
.why-text{top:478px}
.why{top:509px;width:130px;height:80px;background:#fff;border:1px solid var(--line);border-radius:4px}
.why svg{left:11px;top:11px}
.why h3{left:11px;top:29px;font-size:7px;font-weight:600}
.why p{left:11px;top:41px;width:110px;font-size:5.6px;line-height:9.4px;color:var(--ink-soft)}

/* cta */
.cta{left:76px;top:641px;width:413px;height:112px;border-radius:10px;background:var(--teal);overflow:hidden}
.cta .ring{border-radius:50%;background:rgba(255,255,255,.1)}
.cta h2{left:23px;top:24px;font-size:13px;font-weight:700;color:#fff}
.cta p{left:23px;top:48px;width:225px;font-size:6.3px;line-height:10px;color:#dfeceb}
.pill{top:76px;height:13px;border-radius:7px;background:rgba(255,255,255,.14);color:#e8f1f0;font-size:4.6px;display:flex;align-items:center;gap:3px;padding:0 5px}
.pill *{position:static}
.cta-btn{left:301px;top:44px;width:60px;height:25px;border-radius:4px;background:#fff;color:var(--teal);font-size:6.4px;font-weight:700;display:flex;align-items:center;justify-content:center}

/* home footer */
.home-footer{left:0;top:783px;width:100%;height:119px;border-top:1px solid var(--line);background:var(--page)}
.home-footer .brand{left:80px;top:13px}
.foot-about{left:78px;top:41px;width:85px;font-size:4.7px;line-height:7.2px;color:var(--ink-soft)}
.foot-col{top:19px;font-size:4.7px;line-height:7.2px;color:var(--ink-soft)}
.foot-col h4{position:static;font-size:5.6px;font-weight:600;color:var(--ink);margin-bottom:7px}
.foot-col p{position:static;margin-bottom:6px}
.map{left:399px;top:29px;width:93px;height:45px;border-radius:2px;background:linear-gradient(120deg,#b9c6b8 0%,#d9c99a 45%,#caa98a 75%,#bfc4c0 100%)}
.foot-rule{left:78px;top:88px;width:414px;height:1px;background:var(--line)}
.foot-copy{left:78px;top:94px;font-size:4.2px;color:var(--ink-soft)}
.foot-icons{left:458px;top:92px;display:flex;gap:7px}
.foot-icons svg{position:static}

/* booking */
.book-title{left:0;top:41px;width:100%;text-align:center;font-size:12px;font-weight:700;letter-spacing:-.2px}
.book-sub{left:0;top:60px;width:100%;text-align:center;font-size:5.8px;color:var(--ink-soft)}
.progress{left:116px;top:78px;width:333px;height:52px;background:#fff;border:1px solid var(--line);border-radius:4px;box-shadow:0 1px 3px rgba(0,0,0,.04)}
.progress h3{left:8px;top:10px;font-size:5.8px;font-weight:600}
.pct{right:8px;top:9px;height:8px;padding:0 5px;border-radius:4px;background:#e8efef;color:var(--teal);font-size:4.1px;font-weight:700;line-height:8px;letter-spacing:.2px}
.track{left:8px;top:22px;width:316px;height:3px;border-radius:2px;background:var(--track)}
.fill{left:0;top:0;height:3px;border-radius:2px;background:var(--teal)}
.step{top:30px;font-size:3.9px;color:var(--muted);text-align:center;width:40px}
.step.on{color:var(--teal);font-weight:600}
.step i{left:18px;top:7px;width:4px;height:4px;border-radius:50%;background:#dde4e7}
.step.on i{background:var(--teal)}
.block-title{left:116px;display:flex;align-items:center;gap:4px;font-size:8px;font-weight:500}
.block-title *{position:static}
.appt{top:160px;width:78px;height:99px;background:#fff;border:1px solid var(--line);border-radius:3px}
.appt.selected{border:1px solid var(--teal)}
.appt .art{left:6px;top:5px;width:66px;height:66px;border-radius:2px;background:#eef2f4;display:flex;align-items:center;justify-content:center}
.appt .art svg{position:static}
.appt h4{left:6px;top:78px;font-size:5.6px;font-weight:500}
.appt.selected h4{font-weight:600}
.appt p{left:6px;top:87px;font-size:4.6px;color:var(--muted)}
.divider{left:116px;width:333px;height:1px;background:var(--line)}
.back{left:124px;display:flex;align-items:center;gap:3px;font-size:5.6px;font-weight:500;color:var(--ink)}
.back *{position:static}
.next{left:389px;width:60px;height:17px;border-radius:2px;background:var(--teal);color:#fff;font-size:5.6px;font-weight:600;display:flex;align-items:center;justify-content:center;gap:3px;box-shadow:0 2px 4px rgba(0,0,0,.12)}
.next *{position:static}
.book-footer{left:0;width:100%;height:30px;background:#fff}
.book-footer .copy{left:116px;top:13px;font-size:4.5px;color:var(--ink-soft)}
.book-footer .links{right:114px;top:13px;display:flex;gap:8px;font-size:4.5px;color:var(--muted)}
.book-footer .links *{position:static}
.view-all{right:116px;top:148px;font-size:4.6px;color:var(--teal);font-weight:500}
.doc{width:163px;height:40px;background:#fff;border:1px solid var(--line);border-radius:3px}
.doc .photo{left:5px;top:5px;width:28px;height:28px;border-radius:2px}
.doc h4{left:40px;top:9px;font-size:6.2px;font-weight:500}
.doc .role{left:40px;top:18px;font-size:4.6px;color:var(--ink-soft)}
.doc .rate{left:40px;top:26px;font-size:3.9px;color:var(--ink-soft);display:flex;align-items:center;gap:2px}
.doc .rate *{position:static}
.doc .go{right:6px;top:13px;width:12px;height:12px;border-radius:2px;background:#f1f4f5;display:flex;align-items:center;justify-content:center}
.doc .go svg{position:static}
</style>
</head>
<body>

<svg width="0" height="0" style="position:absolute">
  <defs>
    <symbol id="i-steth" viewBox="0 0 24 24"><path d="M5 3v5a5 5 0 0 0 10 0V3M10 13v2a5 5 0 0 0 10 0v-2" fill="none" stroke="currentColor" stroke-width="1.8" stroke-linecap="round"/><circle cx="20" cy="11" r="2" fill="none" stroke="currentColor" stroke-width="1.8"/></symbol>
    <symbol id="i-brain" viewBox="0 0 24 24"><path d="M12 4a3 3 0 0 0-5 1 3 3 0 0 0-2 5 3 3 0 0 0 1 5 3 3 0 0 0 6 3zM12 4a3 3 0 0 1 5 1 3 3 0 0 1 2 5 3 3 0 0 1-1 5 3 3 0 0 1-6 3zM12 4v16M8 10h2M14 13h2" fill="none" stroke="currentColor" stroke-width="1.6" stroke-linecap="round" stroke-linejoin="round"/></symbol>
    <symbol id="i-doc" viewBox="0 0 24 24"><path d="M6 3h8l4 4v14H6zM14 3v4h4M9 12h6M9 15h6M9 18h4" fill="none" stroke="currentColor" stroke-width="1.6" stroke-linejoin="round" stroke-linecap="round"/></symbol>
    <symbol id="i-syringe" viewBox="0 0 24 24"><path d="M18 2l4 4M20 4l-4 4M16 4l4 4M17 7L8 16l-2-2 9-9M6 14l-3 3M9 11l2 2M11 9l2 2M6 16l2 2-4 4" fill="none" stroke="currentColor" stroke-width="1.6" stroke-linecap="round"/></symbol>
    <symbol id="i-heart" viewBox="0 0 24 24"><path d="M12 20s-8-4.6-8-10a4.5 4.5 0 0 1 8-2.8A4.5 4.5 0 0 1 20 10c0 5.4-8 10-8 10z" fill="none" stroke="currentColor" stroke-width="1.8" stroke-linejoin="round"/></symbol>
    <symbol id="i-shield" viewBox="0 0 24 24"><path d="M12 3l7 3v6c0 4.5-3 7.5-7 9-4-1.5-7-4.5-7-9V6z" fill="none" stroke="currentColor" stroke-width="1.8" stroke-linejoin="round"/><path d="M9 12l2 2 4-4" fill="none" stroke="currentColor" stroke-width="1.8" stroke-linecap="round"/></symbol>
    <symbol id="i-spark" viewBox="0 0 24 24"><path d="M10 4l1.6 4.4L16 10l-4.4 1.6L10 16l-1.6-4.4L4 10l4.4-1.6zM18 3v4M16 5h4M6 17v4M4 19h4" fill="none" stroke="currentColor" stroke-width="1.6" stroke-linejoin="round" stroke-linecap="round"/></symbol>
    <symbol id="i-tube" viewBox="0 0 24 24"><path d="M9 3h6M10 3v14a2 2 0 0 0 4 0V3M10 11h4" fill="none" stroke="currentColor" stroke-width="1.8" stroke-linecap="round"/></symbol>
    <symbol id="i-smile" viewBox="0 0 24 24"><circle cx="12" cy="12" r="8" fill="none" stroke="currentColor" stroke-width="1.8"/><path d="M9 14a4 4 0 0 0 6 0" fill="none" stroke="currentColor" stroke-width="1.8" stroke-linecap="round"/><circle cx="9" cy="10" r="1" fill="currentColor"/><circle cx="15" cy="10" r="1" fill="currentColor"/></symbol>
    <symbol id="i-user" viewBox="0 0 24 24"><circle cx="12" cy="8" r="4" fill="none" stroke="currentColor" stroke-width="2"/><path d="M4 21a8 8 0 0 1 16 0" fill="none" stroke="currentColor" stroke-width="2" stroke-linecap="round"/></symbol>
    <symbol id="i-users" viewBox="0 0 24 24"><circle cx="9" cy="8" r="4" fill="none" stroke="currentColor" stroke-width="2"/><path d="M2 21a7 7 0 0 1 14 0M16 4a4 4 0 0 1 0 8M19 14a6 6 0 0 1 3 7" fill="none" stroke="currentColor" stroke-width="2" stroke-linecap="round"/></symbol>
    <symbol id="i-left" viewBox="0 0 24 24"><path d="M19 12H5M11 6l-6 6 6 6" fill="none" stroke="currentColor" stroke-width="2.2" stroke-linecap="round" stroke-linejoin="round"/></symbol>
    <symbol id="i-right" viewBox="0 0 24 24"><path d="M5 12h14M13 6l6 6-6 6" fill="none" stroke="currentColor" stroke-width="2.2" stroke-linecap="round" stroke-linejoin="round"/></symbol>
    <symbol id="i-chev" viewBox="0 0 24 24"><path d="M9 5l7 7-7 7" fill="none" stroke="currentColor" stroke-width="2.4" stroke-linecap="round" stroke-linejoin="round"/></symbol>
    <symbol id="i-clock" viewBox="0 0 24 24"><circle cx="12" cy="12" r="9" fill="none" stroke="currentColor" stroke-width="2"/><path d="M12 7v5l3 2" fill="none" stroke="currentColor" stroke-width="2" stroke-linecap="round"/></symbol>
    <symbol id="i-phone" viewBox="0 0 24 24"><path d="M5 3h4l2 5-3 2a11 11 0 0 0 6 6l2-3 5 2v4a2 2 0 0 1-2 2A17 17 0 0 1 3 5a2 2 0 0 1 2-2z" fill="none" stroke="currentColor" stroke-width="2" stroke-linejoin="round"/></symbol>
    <symbol id="i-globe" viewBox="0 0 24 24"><circle cx="12" cy="12" r="9" fill="none" stroke="currentColor" stroke-width="2"/><path d="M3 12h18M12 3a14 14 0 0 1 0 18M12 3a14 14 0 0 0 0 18" fill="none" stroke="currentColor" stroke-width="2"/></symbol>
    <symbol id="i-share" viewBox="0 0 24 24"><circle cx="18" cy="5" r="3" fill="none" stroke="currentColor" stroke-width="2"/><circle cx="6" cy="12" r="3" fill="none" stroke="currentColor" stroke-width="2"/><circle cx="18" cy="19" r="3" fill="none" stroke="currentColor" stroke-width="2"/><path d="M8.6 10.5l6.8-4M8.6 13.5l6.8 4" fill="none" stroke="currentColor" stroke-width="2"/></symbol>
    <symbol id="i-star" viewBox="0 0 24 24"><path d="M12 2l3 7 7 .6-5.3 4.7 1.6 7.2L12 17.8 5.7 21.5l1.6-7.2L2 9.6 9 9z" fill="currentColor"/></symbol>
  </defs>
</svg>

<!-- Home page -->
<section class="panel home">
  <header class="site-header">
    <div class="brand"><span class="brand-mark"></span><span class="brand-name">Marbleton Health Group</span></div>
    <nav class="nav"><span>Services</span><span>Doctors</span><span>About</span><span>Contact</span></nav>
    <div class="btn-nav">Book Now</div>
  </header>

  <div class="badge">TRUSTED HEALTHCARE</div>
  <h1 class="hero-title">Compassion<br>ate Care for<br>Your Family</h1>
  <p class="hero-text">Experience world-class healthcare with a personal touch. Our expert team is dedicated to your family's long-term well-being and preventive health.</p>
  <div class="btn-primary">Book Appointment</div>
  <div class="btn-ghost">View Services</div>
  <div class="hero-rule"></div>
  <div class="patients">
    <span class="dot-face" role="img" aria-label="Patient portrait" style="background:#6b5a4e"></span>
    <span class="dot-face" role="img" aria-label="Patient portrait" style="background:#4d5d73"></span>
    <span class="dot-face" role="img" aria-label="Patient portrait" style="background:#a9b1b5"></span>
    <p>Joined by <b>15,000+</b>happy patients</p>
  </div>
  <div class="hero-photo" role="img" aria-label="Bright clinic wall with a potted olive tree and a framed letter board sign"></div>

  <h2 class="section-title">Our Services</h2>
  <div class="section-bar"></div>

  <article class="svc" style="left:76px"><div class="ico"><svg width="10" height="10" style="color:var(--teal)"><use href="#i-steth"/></svg></div><h3>General Practice</h3><p>Comprehensive health checkups and preventative care for all ages.</p></article>
  <article class="svc" style="left:181px"><div class="ico"><svg width="10" height="10" style="color:var(--teal)"><use href="#i-smile"/></svg></div><h3>Pediatrics</h3><p>Specialized medical care for infants, children, and adolescents.</p></article>
  <article class="svc" style="left:287px"><div class="ico"><svg width="10" height="10" style="color:var(--teal)"><use href="#i-heart"/></svg></div><h3>Cardiology</h3><p>Advanced heart health monitoring and specialized diagnostic services.</p></article>
  <article class="svc" style="left:392px"><div class="ico"><svg width="10" height="10" style="color:var(--teal)"><use href="#i-tube"/></svg></div><h3>Laboratory</h3><p>Quick and accurate diagnostic testing and comprehensive blood work.</p></article>

  <div class="why-band"></div>
  <h2 class="why-title">Why Families Choose Marbleton<br>Health Group</h2>
  <p class="why-text">We combine medical expertise with a patient-first approach to provide<br>the best care possible in your community.</p>

  <article class="why" style="left:76px"><svg width="11" height="11" style="color:var(--teal)"><use href="#i-shield"/></svg><h3>Expert Doctors</h3><p>Our board-certified specialists have over 15+ years of experience in their respective medical fields.</p></article>
  <article class="why" style="left:217px"><svg width="11" height="11" style="color:var(--teal)"><use href="#i-spark"/></svg><h3>Modern Facilities</h3><p>Equipped with the latest diagnostic technology ensuring high precision and faster treatment paths.</p></article>
  <article class="why" style="left:359px"><svg width="11" height="11" style="color:var(--teal)"><use href="#i-heart"/></svg><h3>Patient-Centered</h3><p>We listen to your concerns and customize health plans that fit your lifestyle and specific needs.</p></article>

  <section class="cta">
    <span class="ring" style="left:367px;top:-34px;width:80px;height:80px"></span>
    <span class="ring" style="left:-20px;top:88px;width:44px;height:44px"></span>
    <h2>Ready to prioritize your health?</h2>
    <p>Book an appointment online in less than 2 minutes. Our team is ready to welcome you to our modern clinic.</p>
    <div class="pill" style="left:23px"><svg width="5" height="5"><use href="#i-clock"/></svg><span>Open Mon-Sat</span></div>
    <div class="pill" style="left:82px"><svg width="5" height="5"><use href="#i-phone"/></svg><span>(555) 010-2283</span></div>
    <div class="cta-btn">Book Now</div>
  </section>

  <footer class="home-footer">
    <div class="brand"><span class="brand-mark"></span><span class="brand-name">Marbleton Health Group</span></div>
    <p class="foot-about">Providing exceptional medical services with heart and excellence since 1998.</p>
    <div class="foot-col" style="left:185px"><h4>Contact</h4><p>48 Larkspur Row, Suite 210<br>Eastfield, NY 10877</p><p>hello@marbletonhealth.com</p></div>
    <div class="foot-col" style="left:292px"><h4>Quick Links</h4><p>Patient Portal</p><p>Insurance Info</p><p>Privacy Policy</p></div>
    <div class="foot-col" style="left:399px"><h4>Location</h4></div>
    <div class="map" role="img" aria-label="Map showing the clinic location"></div>
    <div class="foot-rule"></div>
    <p class="foot-copy">© Marbleton Health Group. All rights reserved.</p>
    <div class="foot-icons" style="color:var(--ink-soft)"><svg width="7" height="7"><use href="#i-globe"/></svg><svg width="7" height="7"><use href="#i-heart"/></svg><svg width="7" height="7"><use href="#i-share"/></svg></div>
  </footer>
</section>

<!-- Booking step 1 -->
<section class="panel book-one">
  <header class="site-header">
    <div class="brand"><span class="brand-mark"></span><span class="brand-name">Marbleton Health Group</span></div>
    <nav class="nav"><span>Home</span><span>Services</span><span>Doctors</span><span class="active">Booking</span></nav>
    <div class="avatar-btn"><svg width="6" height="6" style="color:var(--ink-soft)"><use href="#i-user"/></svg></div>
  </header>
  <h1 class="book-title">Book Your Appointment</h1>
  <p class="book-sub">Schedule a visit with our specialists in just a few minutes.</p>

  <div class="progress">
    <h3>Step 1: Select Service</h3>
    <span class="pct">25% COMPLETE</span>
    <div class="track"><div class="fill" style="width:79px"></div></div>
    <div class="step on" style="left:-4px">Service<i></i></div>
    <div class="step" style="left:102px">Doctor<i></i></div>
    <div class="step" style="left:198px">Time<i></i></div>
    <div class="step" style="left:299px">Patient Info<i></i></div>
  </div>

  <div class="block-title" style="top:142px"><svg width="8" height="8" style="color:var(--teal)"><use href="#i-steth"/></svg><span>Type of Appointment</span></div>

  <article class="appt selected" style="left:116px"><div class="art"><svg width="14" height="14" style="color:var(--teal)"><use href="#i-steth"/></svg></div><h4>General Consultation</h4><p>30 min • $50</p></article>
  <article class="appt" style="left:201px"><div class="art"><svg width="14" height="14" style="color:var(--teal)"><use href="#i-brain"/></svg></div><h4>Specialist Visit</h4><p>45 min • $120</p></article>
  <article class="appt" style="left:286px"><div class="art"><svg width="14" height="14" style="color:var(--teal)"><use href="#i-doc"/></svg></div><h4>Follow-up</h4><p>20 min • $30</p></article>
  <article class="appt" style="left:370px"><div class="art"><svg width="14" height="14" style="color:var(--teal)"><use href="#i-syringe"/></svg></div><h4>Vaccination</h4><p>15 min • $25</p></article>

  <div class="divider" style="top:290px"></div>
  <div class="back" style="top:301px"><svg width="6" height="6"><use href="#i-left"/></svg><span>Back</span></div>
  <div class="next" style="top:295px"><span>Next Step</span><svg width="6" height="6"><use href="#i-right"/></svg></div>

  <footer class="book-footer" style="top:345px">
    <p class="copy">© 2024 Marbleton Health Group. All rights reserved.</p>
    <div class="links"><span>Privacy Policy</span><span>Terms of Service</span><span>Contact Support</span></div>
  </footer>
</section>

<!-- Booking step 2 -->
<section class="panel book-two">
  <header class="site-header">
    <div class="brand"><span class="brand-mark"></span><span class="brand-name">Marbleton Health Group</span></div>
    <nav class="nav"><span>Home</span><span>Services</span><span>Doctors</span><span class="active">Booking</span></nav>
    <div class="avatar-btn"><svg width="6" height="6" style="color:var(--ink-soft)"><use href="#i-user"/></svg></div>
  </header>
  <h1 class="book-title">Book Your Appointment</h1>
  <p class="book-sub">Schedule a visit with our specialists in just a few minutes.</p>

  <div class="progress">
    <h3>Step 2: Choose Doctor</h3>
    <span class="pct">50% COMPLETE</span>
    <div class="track"><div class="fill" style="width:158px"></div></div>
    <div class="step on" style="left:-4px">Service<i></i></div>
    <div class="step on" style="left:102px">Doctor<i></i></div>
    <div class="step" style="left:198px">Time<i></i></div>
    <div class="step" style="left:299px">Patient Info<i></i></div>
  </div>

  <div class="block-title" style="top:146px"><svg width="8" height="8" style="color:var(--teal)"><use href="#i-users"/></svg><span>Available Doctors</span></div>
  <span class="view-all">View All Doctors</span>

  <article class="doc" style="left:116px;top:159px"><div class="photo" role="img" aria-label="Portrait of Dr. Nora Halvorsen" style="background:linear-gradient(160deg,#cfd3d4,#3a3532)"></div><h4>Dr. Nora Halvorsen</h4><span class="role">Internal Medicine</span><span class="rate"><svg width="4" height="4" style="color:var(--star)"><use href="#i-star"/></svg><span>4.9 (124 reviews)</span></span><span class="go"><svg width="5" height="5"><use href="#i-chev"/></svg></span></article>
  <article class="doc" style="left:285px;top:159px"><div class="photo" role="img" aria-label="Portrait of Dr. Felix Amari" style="background:linear-gradient(160deg,#c7cdd2,#3e4e66)"></div><h4>Dr. Felix Amari</h4><span class="role">Cardiology Specialist</span><span class="rate"><svg width="4" height="4" style="color:var(--star)"><use href="#i-star"/></svg><span>4.8 (89 reviews)</span></span><span class="go"><svg width="5" height="5"><use href="#i-chev"/></svg></span></article>
  <article class="doc" style="left:116px;top:205px"><div class="photo" role="img" aria-label="Portrait of Dr. Ines Castellano" style="background:linear-gradient(160deg,#d6dbdc,#2f9aa6)"></div><h4>Dr. Ines Castellano</h4><span class="role">Pediatrics</span><span class="rate"><svg width="4" height="4" style="color:var(--star)"><use href="#i-star"/></svg><span>5 (210 reviews)</span></span><span class="go"><svg width="5" height="5"><use href="#i-chev"/></svg></span></article>
  <article class="doc" style="left:285px;top:205px"><div class="photo" role="img" aria-label="Portrait of Dr. Owen Bratt" style="background:linear-gradient(160deg,#d9dcdd,#8d9396)"></div><h4>Dr. Owen Bratt</h4><span class="role">Dermatologist</span><span class="rate"><svg width="4" height="4" style="color:var(--star)"><use href="#i-star"/></svg><span>4.7 (56 reviews)</span></span><span class="go"><svg width="5" height="5"><use href="#i-chev"/></svg></span></article>

  <div class="divider" style="top:273px"></div>
  <div class="back" style="top:289px"><svg width="6" height="6"><use href="#i-left"/></svg><span>Back</span></div>
  <div class="next" style="top:282px"><span>Next Step</span><svg width="6" height="6"><use href="#i-right"/></svg></div>

  <footer class="book-footer" style="top:333px">
    <p class="copy">© 2024 Marbleton Health Group. All rights reserved.</p>
    <div class="links"><span>Privacy Policy</span><span>Terms of Service</span><span>Contact Support</span></div>
  </footer>
</section>

</body>
</html>
```